Director of Sustainability Education Programs at WR
Dwight K. Pellham Professor, Systems Design
Director of Sustainability Education Programs at WR -
Creative Brief
Professional
Marcus R. Varmonde
Director of Balanced Technology Learning, School of Engineering
4170 HL Tessard Building 1860 Quillon Avenue Ann Arbor, MI 48107-3391
varmonde@wrolvaine.edu
http://cobt.tekn.wrolvaine.edu
Title has multiple lines Director of Balanced Technology Learning, School of Engineering Dwight K. Pellham Professor, Systems Design University of Wrolvaine

```html
<!DOCTYPE html>
<html lang="en">
<head>
<meta charset="utf-8">
<title>Marcus R. Varmonde – Business Card</title>
<link href="https://fonts.googleapis.com/css2?family=Open+Sans:wght@400;600;700&display=swap" rel="stylesheet">
<style>
  :root {
    --page-bg: #e9e6e1;
    --card-white: #ffffff;
    --brand-blue: #2e66ae;
    --brand-blue-dark: #1f4f8f;
    --brand-green: #7dba3f;
    --ink: #2b3a55;
    --ink-soft: #5b6577;
  }
  * { box-sizing: border-box; margin: 0; padding: 0; }
  html, body { width: 1200px; height: 739px; overflow: hidden; }
  body {
    background: var(--page-bg);
    font-family: "Open Sans", Arial, sans-serif;
    position: relative;
  }
  .card {
    position: absolute;
    width: 520px;
    height: 297px;
    background: var(--card-white);
    box-shadow: 0 6px 18px rgba(0,0,0,0.18);
    overflow: hidden;
  }
  .card--front { left: 50px; top: 221px; }
  .card--back { left: 630px; top: 221px; }

  /* Front */
  .brand-lockup {
    position: absolute;
    left: 0; right: 0; top: 92px;
    display: flex; flex-direction: column; align-items: center; gap: 10px;
  }
  .brand-mark {
    width: 34px; height: 34px; border-radius: 50%;
    background: var(--brand-green);
    flex: none;
  }
  .brand-name {
    font-weight: 700; font-size: 17px; color: var(--brand-blue);
    letter-spacing: 0.5px; text-transform: uppercase;
  }
  .front-url {
    position: absolute; left: 0; right: 0; top: 196px;
    text-align: center; font-size: 12px; color: var(--ink);
  }

  /* Back */
  .wave { position: absolute; inset: 0; }
  .holder {
    position: absolute; left: 20px; top: 34px; width: 290px;
    text-align: center;
  }
  .holder-name {
    font-size: 18px; font-weight: 700; color: var(--brand-blue);
    margin-bottom: 6px;
  }
  .holder-title {
    font-size: 8.5px; line-height: 1.45; color: var(--ink-soft);
  }
  .back-lockup {
    position: absolute; left: 30px; bottom: 40px;
    display: flex; align-items: center; gap: 10px;
  }
  .back-lockup .brand-mark { width: 26px; height: 26px; }
  .back-lockup .brand-name { font-size: 12px; line-height: 1.2; max-width: 170px; }
  .contact {
    position: absolute; right: 24px; top: 52px;
    text-align: right; color: var(--card-white);
    font-size: 8.5px; line-height: 1.55; font-style: normal;
  }
  .contact .gap { height: 8px; }
  .contact-url {
    position: absolute; right: 24px; bottom: 26px;
    color: var(--card-white); font-size: 10px; font-weight: 600;
  }
</style>
</head>
<body>

<section class="card card--front" aria-label="Card front">
  <div class="brand-lockup">
    <span class="brand-mark"></span>
    <span class="brand-name">Center on Balanced Technology</span>
  </div>
  <p class="front-url">http://cobt.tekn.wrolvaine.edu</p>
</section>

<section class="card card--back" aria-label="Card back">
  <svg class="wave" viewBox="0 0 520 297" preserveAspectRatio="none" aria-hidden="true">
    <path d="M350 0 C300 90 330 170 250 230 C200 268 130 285 60 297 L520 297 L520 0 Z" fill="var(--brand-green)"/>
    <path d="M362 0 C318 92 346 175 268 236 C218 272 150 287 90 297 L520 297 L520 0 Z" fill="var(--card-white)"/>
    <path d="M372 0 C330 95 360 180 282 240 C236 274 170 289 120 297 L520 297 L520 0 Z" fill="var(--brand-blue)"/>
    <path d="M440 0 C410 80 430 150 380 210 C350 250 300 280 260 297 L520 297 L520 0 Z" fill="var(--brand-blue-dark)" opacity="0.25"/>
  </svg>

  <div class="holder">
    <h1 class="holder-name">Marcus R. Varmonde</h1>
    <p class="holder-title">
      Director of Balanced Technology Learning, School of Engineering<br>
      Dwight K. Pellham Professor, Systems Design<br>
      University of Wrolvaine
    </p>
  </div>

  <div class="back-lockup">
    <span class="brand-mark"></span>
    <span class="brand-name">Center on Balanced Technology</span>
  </div>

  <address class="contact">
    4170 HL Tessard Building<br>
    1860 Quillon Avenue<br>
    Larkmont, OR 97391
    <div class="gap"></div>
    Tel 555-0142<br>
    Fax 555-0178<br>
    varmonde@wrolvaine.edu
  </address>
  <p class="contact-url">http://cobt.tekn.wrolvaine.edu</p>
</section>

</body>
</html>
```